We need a business card design for Corvana Group. We are a healthcare recruiting, wellness and education company. We partner with medical facilities to find quality candidates. We also offer free wellness courses.
The final design should communicate an emphasis on recruiting and wellness
The main purpose of the business card is to utilized it for networking events, give to hospitals, executives, VCs surgery centers and clinics. I want it to be sleek, clean, use of our brand colors and professional.

```html
<!DOCTYPE html>
<html lang="en">
<head>
<meta charset="utf-8">
<title>Corvana Group – Business Card</title>
<link href="https://fonts.googleapis.com/css2?family=Newsreader:ital,opsz,wght@0,6..72,400;1,6..72,400&family=Roboto:wght@300;400&display=swap" rel="stylesheet">
<style>
  :root {
    --backdrop: #979797;
    --brand-green: #025a4c;
    --brand-mist: #e4eeec;
    --brand-blush: #f4aaa2;
    --card-paper: #ececea;
    --ink-dark: #0f2e28;
    --ink-muted: #5f6462;
    --rule: #9a9d9b;
  }
  * { box-sizing: border-box; margin: 0; padding: 0; }
  html, body {
    width: 1200px;
    height: 1200px;
    overflow: hidden;
    background: var(--backdrop);
  }
  .card {
    position: absolute;
    left: 225px;
    width: 746px;
    height: 436px;
  }
  .card-front {
    top: 134px;
    background: var(--brand-green);
    border-radius: 0 62px 0 62px;
  }
  .card-back {
    top: 622px;
    background: var(--card-paper);
    border-radius: 62px 0 62px 0;
  }
  .front-brand {
    position: absolute;
    left: 0;
    right: 0;
    top: 160px;
    display: flex;
    justify-content: center;
    align-items: center;
    gap: 18px;
    font-family: "Roboto", sans-serif;
    font-weight: 400;
    font-size: 64px;
    letter-spacing: 1px;
    color: var(--brand-mist);
  }
  .brand-square {
    width: 34px;
    height: 34px;
    border-radius: 6px;
    background: var(--brand-mist);
  }
  .tagline {
    position: absolute;
    left: 0;
    right: 0;
    top: 354px;
    text-align: center;
    font-family: "Newsreader", serif;
    font-style: italic;
    font-size: 25px;
    color: var(--brand-blush);
  }
  .back-brand {
    position: absolute;
    left: 0;
    right: 0;
    top: 68px;
    display: flex;
    justify-content: center;
    align-items: center;
    gap: 12px;
    font-family: "Roboto", sans-serif;
    font-weight: 400;
    font-size: 40px;
    color: var(--brand-green);
  }
  .back-brand .brand-square {
    width: 26px;
    height: 26px;
    border-radius: 5px;
    background: var(--brand-green);
  }
  .identity {
    position: absolute;
    right: 410px;
    top: 218px;
    text-align: right;
  }
  .person-name {
    font-family: "Newsreader", serif;
    font-size: 40px;
    line-height: 1.1;
    color: var(--brand-green);
  }
  .person-role {
    font-family: "Roboto", sans-serif;
    font-size: 20px;
    color: var(--ink-dark);
    margin-top: 2px;
  }
  .divider {
    position: absolute;
    left: 354px;
    top: 220px;
    width: 1px;
    height: 73px;
    background: var(--rule);
  }
  .contact-list {
    position: absolute;
    left: 374px;
    top: 216px;
    list-style: none;
    font-family: "Roboto", sans-serif;
    font-weight: 300;
    font-size: 20px;
    line-height: 27px;
    color: var(--ink-muted);
  }
  .location {
    position: absolute;
    left: 0;
    right: 0;
    top: 390px;
    display: flex;
    justify-content: center;
    align-items: center;
    gap: 8px;
    font-family: "Roboto", sans-serif;
    font-weight: 300;
    font-size: 20px;
    color: var(--ink-muted);
  }
  .location svg { width: 12px; height: 17px; fill: var(--ink-muted); }
</style>
</head>
<body>
  <section class="card card-front">
    <div class="front-brand"><span class="brand-square"></span>Corvana</div>
    <p class="tagline">Transforming the healthcare employment experience</p>
  </section>

  <section class="card card-back">
    <div class="back-brand"><span class="brand-square"></span>Corvana Group</div>
    <div class="identity">
      <p class="person-name">Mara Ellison</p>
      <p class="person-role">Co-Founder + CEO</p>
    </div>
    <span class="divider"></span>
    <ul class="contact-list">
      <li>+1 555-018-2740</li>
      <li>mara.ellison@corvanagroup.com</li>
      <li>corvanagroup.com</li>
    </ul>
    <p class="location">
      <svg viewBox="0 0 12 17" aria-hidden="true"><path d="M6 0C2.7 0 0 2.6 0 5.9 0 10.3 6 17 6 17s6-6.7 6-11.1C12 2.6 9.3 0 6 0zm0 8.2a2.3 2.3 0 1 1 0-4.6 2.3 2.3 0 0 1 0 4.6z"/></svg>
      Riverton, Ohio
    </p>
  </section>
</body>
</html>
```